Dog care service needs advertising poster

Our company is Paw Haven. We provide care for dogs while their owners are away, either through home visits or a holiday stay in the homes of carefully selected minders. Our existing website & Facebook cover should provide all the colour cues for a poster - namely blues, blondes and grey. We have an existing logo (provided). We can feature the same imagery from our website as I have purchased the rights to the stock images.

www.pawhavenexample.com.au
www.facebook.com/pawhavenexampleau

This brief is for design of a poster that can be placed in vet surgeries, groomers, on community noticeboards. It should be scalable to print in three sizes, A5, A4 & A3.

We wish to clearly communicate our three areas of service "dog minding, home visits, dog walking".

We would like to have the files ready for upload to Printora (or similar) for immediate printing.

Target Market(s)

Dog owners who love their dogs like family.

Industry/Entity Type

Advertising

Font styles to use
Sans Serif

Colors
33a6d7
3276b5

Requirements
Must have
• Logo
• www.pawhavenexample.com.au
• Telephone number
• Three services - Dog Minding, Home Visits, Dog Walking
Nice to have
• use of our existing stock photography to highlight the three areas of service - Dog minding, home visits, dog walking. Existing colour palette - blues, blondes and grey.
• Text that can be used:
• Western Sydney’s complete dog care service.
• Dog Minding - Your dog stays in the home of one of our carefully selected minders.Treated like part of the family, they enjoy all the creature comforts they are used to.
• Home Visits - We visit your dog at your home for feeding, walking and playtime. Short of long visits available.
• Dog Walking - If you can't walk your dog for any reason we are here to help. 1/2 hour or hourly walks available.
• Contact us today for a tailored package to meet your needs.
Should not have
• Any additional illustrations beyond the logo.

```html
<!DOCTYPE html>
<html lang="en">
<head>
<meta charset="utf-8">
<title>Paw Haven – Dog Care Poster</title>
<link href="https://fonts.googleapis.com/css2?family=Ubuntu:wght@500;700&family=Bitter:wght@500&family=Open+Sans:wght@600&display=swap" rel="stylesheet">
<style>
  :root {
    --navy: #2f3d4f;
    --sky: #33a6d7;
    --royal: #3276b5;
    --deep: #1f5e9e;
    --ink: #333a40;
    --paper: #ffffff;
  }
  html, body { margin: 0; padding: 0; overflow: hidden; background: var(--paper); }
  .poster {
    position: relative;
    width: 1200px;
    height: 848px;
    overflow: hidden;
    background: var(--paper);
  }
  .brand {
    position: absolute;
    left: 66px;
    top: 66px;
    display: flex;
    align-items: center;
    gap: 22px;
  }
  .brand-dot {
    width: 92px;
    height: 92px;
    border-radius: 50%;
    background: var(--navy);
  }
  .brand-name {
    font-family: "Ubuntu", sans-serif;
    font-weight: 700;
    font-size: 64px;
    color: var(--navy);
    line-height: 1;
  }
  .contact {
    position: absolute;
    right: 52px;
    top: 76px;
    text-align: right;
    font-family: "Ubuntu", sans-serif;
    font-weight: 500;
    font-size: 33px;
    line-height: 40px;
    color: var(--sky);
  }
  .intro {
    position: absolute;
    left: 62px;
    top: 226px;
    width: 1100px;
    margin: 0;
    font-family: "Open Sans", sans-serif;
    font-weight: 600;
    font-size: 13.6px;
    line-height: 23px;
    color: var(--ink);
  }
  .wave {
    position: absolute;
    left: 0;
    bottom: 0;
    width: 1200px;
    height: 230px;
  }
  .service {
    position: absolute;
    top: 312px;
    width: 340px;
    text-align: center;
  }
  .service-frame { display: block; margin: 0 auto; }
  .service-title {
    margin: 14px 0 0;
    font-family: "Bitter", serif;
    font-weight: 500;
    font-size: 36px;
    letter-spacing: 0.5px;
    color: var(--royal);
  }
  .service--minding { left: 34px; }
  .service--visits { left: 430px; }
  .service--walking { left: 838px; }
</style>
</head>
<body>
<main class="poster">
  <svg class="wave" viewBox="0 0 1200 230" preserveAspectRatio="none" aria-hidden="true">
    <defs>
      <linearGradient id="wave-fill" x1="0" y1="0" x2="1" y2="0">
        <stop offset="0" stop-color="#3fa3dc"/>
        <stop offset="0.5" stop-color="#1f6fb8"/>
        <stop offset="1" stop-color="#2d8fd3"/>
      </linearGradient>
    </defs>
    <path d="M0 0 C300 60 650 200 1200 120 L1200 230 L0 230 Z" fill="#cfe7f5"/>
    <path d="M0 20 C320 90 640 215 1200 135 L1200 230 L0 230 Z" fill="url(#wave-fill)"/>
    <path d="M0 60 C330 130 700 230 1200 150" fill="none" stroke="#ffffff" stroke-width="5"/>
    <path d="M0 90 C360 160 760 230 1200 178" fill="none" stroke="#8fd0f0" stroke-width="3"/>
    <path d="M380 230 C700 170 950 150 1200 96 L1200 230 Z" fill="#3fa9e0" opacity="0.85"/>
    <path d="M420 230 C720 180 960 165 1200 112" fill="none" stroke="#ffffff" stroke-width="4"/>
  </svg>

  <header class="brand">
    <span class="brand-dot"></span>
    <span class="brand-name">Paw Haven</span>
  </header>

  <div class="contact">
    <div class="contact-web">www.pawhavenexample.com.au</div>
    <div class="contact-phone">Phone: 0491 570 156</div>
  </div>

  <p class="intro">Paw Haven was created to ensure your dog is cared for while you are away, either through daily home visits or a holiday stay with one of our carefully chosen dog minders. Whether it’s one night or many, we are here to ensure your dog receives the love and attention they are used to.</p>

  <section class="service service--minding">
    <svg class="service-frame" width="320" height="330" viewBox="0 0 320 330">
      <defs>
        <radialGradient id="photo-minding" cx="0.5" cy="0.4" r="0.6">
          <stop offset="0" stop-color="#6b5a4c"/>
          <stop offset="0.6" stop-color="#8fae5a"/>
          <stop offset="1" stop-color="#a8d3ea"/>
        </radialGradient>
      </defs>
      <ellipse cx="160" cy="165" rx="148" ry="158" fill="none" stroke="var(--royal)" stroke-width="2.5" transform="rotate(-8 160 165)"/>
      <ellipse cx="158" cy="167" rx="143" ry="153" fill="url(#photo-minding)" role="img" aria-label="Photo of a happy shepherd dog resting in the grass"/>
      <ellipse cx="162" cy="163" rx="150" ry="156" fill="none" stroke="var(--sky)" stroke-width="3" transform="rotate(10 162 163)"/>
    </svg>
    <h2 class="service-title">DOG MINDING</h2>
  </section>

  <section class="service service--visits">
    <svg class="service-frame" width="320" height="330" viewBox="0 0 320 330">
      <defs>
        <linearGradient id="photo-visits" x1="0" y1="0" x2="0" y2="1">
          <stop offset="0" stop-color="#f2f0ec"/>
          <stop offset="0.45" stop-color="#d9c7b0"/>
          <stop offset="1" stop-color="#a27a55"/>
        </linearGradient>
      </defs>
      <ellipse cx="160" cy="165" rx="148" ry="158" fill="none" stroke="var(--royal)" stroke-width="2.5" transform="rotate(-8 160 165)"/>
      <ellipse cx="158" cy="167" rx="143" ry="153" fill="url(#photo-visits)" role="img" aria-label="Photo of a small terrier sitting on a home doormat"/>
      <ellipse cx="162" cy="163" rx="150" ry="156" fill="none" stroke="var(--sky)" stroke-width="3" transform="rotate(10 162 163)"/>
    </svg>
    <h2 class="service-title">HOME VISITS</h2>
  </section>

  <section class="service service--walking">
    <svg class="service-frame" width="320" height="330" viewBox="0 0 320 330">
      <defs>
        <linearGradient id="photo-walking" x1="0" y1="0" x2="0" y2="1">
          <stop offset="0" stop-color="#4f6b3c"/>
          <stop offset="0.5" stop-color="#c9b8a2"/>
          <stop offset="1" stop-color="#5e9a3e"/>
        </linearGradient>
      </defs>
      <ellipse cx="160" cy="165" rx="148" ry="158" fill="none" stroke="var(--royal)" stroke-width="2.5" transform="rotate(-8 160 165)"/>
      <ellipse cx="158" cy="167" rx="143" ry="153" fill="url(#photo-walking)" role="img" aria-label="Photo of a bulldog on a lead walking on a lawn"/>
      <ellipse cx="162" cy="163" rx="150" ry="156" fill="none" stroke="var(--sky)" stroke-width="3" transform="rotate(10 162 163)"/>
    </svg>
    <h2 class="service-title">DOG WALKING</h2>
  </section>
</main>
</body>
</html>
```